Business card por a urban DJ, up scale audience target

Need a sober design, modern, conservative colors but i can consider some options, y play rnb, hip hop, EDM and top40.

Business card for contact and personal info, double sided, use logo attrached please; im 42 so i need a card acording to my age an target audience.

Target Market(s)

Adult people, up scale audience

Industry/Entity Type

Music Download

Contact Information for Business Card

Cel (318) 5024471963 www.kelvarodun.com

Requirements
Must have
• open mind
Nice to have
• open mind
Should not have
• DJ

```html
<!DOCTYPE html>
<html lang="en">
<head>
<meta charset="utf-8">
<title>Kelvaro Business Card</title>
<link rel="stylesheet" href="https://fonts.googleapis.com/css2?family=Jost:wght@400;600&display=swap">
<style>
  :root {
    --page-bg: #e6e4e1;
    --card-white: #ffffff;
    --ink-dark: #1b1b1b;
    --ink-mid: #2c2c2c;
    --band-dark: #161616;
    --band-light: #383838;
    --fold-grey: #8c8c8c;
    --fold-light: #d9d9d9;
    --text-light: #f2f2f2;
    --text-muted: #cfcfcf;
  }
  * { margin: 0; padding: 0; box-sizing: border-box; }
  html, body {
    width: 1200px;
    height: 950px;
    overflow: hidden;
    background: var(--page-bg);
    font-family: "Jost", "Futura", sans-serif;
  }
  .stage {
    width: 1200px;
    height: 950px;
    display: flex;
    align-items: center;
    justify-content: center;
  }
  .business-card {
    position: relative;
    width: 840px;
    height: 480px;
    background: var(--card-white);
    box-shadow: 0 18px 40px rgba(0, 0, 0, 0.18);
    overflow: hidden;
  }
  .brand {
    position: absolute;
    left: 150px;
    top: 120px;
    display: flex;
    align-items: center;
    gap: 18px;
  }
  .brand-mark {
    width: 26px;
    height: 26px;
    background: var(--ink-mid);
  }
  .brand-name {
    font-weight: 600;
    font-size: 74px;
    letter-spacing: 6px;
    color: var(--ink-mid);
    line-height: 1;
  }
  .info-band {
    position: absolute;
    left: 300px;
    right: 0;
    top: 300px;
    height: 140px;
    background: linear-gradient(90deg, var(--band-dark), var(--band-light));
    padding: 30px 0 0 40px;
    color: var(--text-light);
  }
  .info-fold {
    position: absolute;
    right: 0;
    top: 300px;
    width: 70px;
    height: 70px;
  }
  .person {
    font-size: 30px;
    letter-spacing: 1px;
    line-height: 1.2;
  }
  .person-name { font-weight: 600; }
  .person-role { font-weight: 400; }
  .contact {
    margin-top: 10px;
    font-size: 22px;
    font-weight: 400;
    color: var(--text-muted);
    letter-spacing: 0.5px;
  }
  .contact-divider { margin: 0 10px; }
</style>
</head>
<body>
  <main class="stage">
    <section class="business-card">
      <div class="brand">
        <span class="brand-mark"></span>
        <span class="brand-name">KELVARO</span>
      </div>
      <div class="info-band">
        <p class="person"><span class="person-name">MARCO VELL</span> <span class="person-role">- CEO/FOUNDER</span></p>
        <p class="contact">(318) 5024471963<span class="contact-divider">|</span>www.kelvarodun.com</p>
      </div>
      <svg class="info-fold" viewBox="0 0 70 70" aria-hidden="true">
        <defs>
          <linearGradient id="foldShade" x1="0" y1="0" x2="1" y2="1">
            <stop offset="0" stop-color="var(--fold-light)"/>
            <stop offset="1" stop-color="var(--fold-grey)"/>
          </linearGradient>
        </defs>
        <polygon points="0,0 70,0 70,70" fill="url(#foldShade)"/>
      </svg>
    </section>
  </main>
</body>
</html>
```